GRAPHIC DESIGN FOR RESTAURANT MENU FOR HEALTHY RESTAURANT

I am looking for a graphic design for our menu displayed on a TV screen. Please ensure the file will fit on a TV screen nicely. We are looking for a clean design , with the following items. We would also like to include a couple of photos.
Breakfast:
Protein Chocolate Chip Pancakes - $12.95
Sunny Trail Burrito- $11.95
Tall Barn Omelette - $12.95
Lunch
Butter Chicken - $13.95
Chicken Quesadilla - $13.45
Coconut Garlic Shrimp - $15.95
Goat Cheese Stuffed Chicken - $14.95
Chipotle Steak Wrap - $12.95
Turkey Meatball Fettuccini - $13.45
Chicken Alfredo - $13.45
Chicken Parmesan - $13.95
Pesto Chicken Pasta - $13.45
Steak Bite and Green Stir Fry - $13.45
Asian Chicken Teriyaki - $13.45
Please include our logo
Restaurant

```html
<!DOCTYPE html>
<html lang="en">
<head>
<meta charset="UTF-8">
<title>Verdant Table Menu</title>
<link href="https://fonts.googleapis.com/css2?family=Montserrat:wght@500;700&family=Kaushan+Script&display=swap" rel="stylesheet">
<style>
  :root {
    --page-bg: #f1f1f1;
    --arch-white: #ffffff;
    --arch-light: #c2dc6e;
    --arch-dark: #95c221;
    --brand-green: #8cbf26;
    --ink: #3e4349;
    --script-ink: #4b5056;
  }
  * { margin: 0; padding: 0; box-sizing: border-box; }
  html, body {
    width: 750px; height: 1200px; overflow: hidden;
    background: var(--page-bg);
  }
  .menu-board {
    position: absolute; left: 37.5px; top: 0;
    width: 675px; height: 1200px; overflow: hidden;
    font-family: "Montserrat", Arial, sans-serif;
  }
  .food-photo {
    position: absolute; inset: 0;
    background:
      linear-gradient(180deg,
        #e4e9ec 0%, #dfe6ea 22%, #eeeeee 30%,
        #d9573a 45%, #e0633f 60%, #e79a6c 75%,
        #eeeeee 84%, #dbe3e8 92%, #cfd9df 100%);
  }
  .arch {
    position: absolute; left: 162px; width: 350px;
    border-radius: 175px 175px 0 0;
  }
  .arch-brand { top: 54px; height: 1109px; background: var(--arch-white); }
  .arch-breakfast { top: 232px; height: 931px; background: var(--arch-light); }
  .arch-lunch { top: 530px; height: 633px; background: var(--arch-dark); }

  .brand {
    position: absolute; left: 162px; width: 350px; top: 160px;
    text-align: center;
  }
  .brand-name {
    font-weight: 700; font-size: 27px; letter-spacing: 1px;
    color: var(--brand-green); line-height: 1;
  }
  .brand-tagline {
    margin-top: 7px; font-weight: 700; font-size: 10.5px;
    color: var(--brand-green); letter-spacing: 0.2px;
  }
  .section-title {
    position: absolute; left: 162px; width: 350px; text-align: center;
    font-family: "Kaushan Script", cursive;
    font-size: 46px; color: var(--script-ink); font-weight: 400;
    line-height: 1;
  }
  .title-breakfast { top: 318px; }
  .title-lunch { top: 614px; }

  .menu-list { position: absolute; left: 190px; width: 296px; list-style: none; }
  .menu-item {
    position: absolute; left: 0; width: 100%;
    display: flex; justify-content: space-between;
    font-weight: 500; font-size: 13.5px; color: var(--ink);
    line-height: 1; transform: translateY(-50%);
  }
</style>
</head>
<body>
<main class="menu-board">
  <div class="food-photo" role="img" aria-label="Photo of fettuccine with tomato sauce, broccoli and grated parmesan in a white bowl on a whitewashed wooden table"></div>

  <div class="arch arch-brand"></div>
  <div class="arch arch-breakfast"></div>
  <div class="arch arch-lunch"></div>

  <header class="brand">
    <div class="brand-name">VERDANT TABLE</div>
    <div class="brand-tagline">HEALTHY KITCHEN &nbsp;|&nbsp; MEAL PREP</div>
  </header>

  <h2 class="section-title title-breakfast">Breakfast</h2>
  <ul class="menu-list">
    <li class="menu-item" style="top:428px"><span>Protein Chocolate Chip Pancakes</span><span>$12.95</span></li>
    <li class="menu-item" style="top:462px"><span>Sunny Trail Burrito</span><span>$11.95</span></li>
    <li class="menu-item" style="top:495px"><span>Tall Barn Omelette</span><span>$12.95</span></li>
  </ul>

  <h2 class="section-title title-lunch">Lunch</h2>
  <ul class="menu-list">
    <li class="menu-item" style="top:706px"><span>Butter Chicken</span><span>$13.95</span></li>
    <li class="menu-item" style="top:743px"><span>Chicken Quesadilla</span><span>$13.45</span></li>
    <li class="menu-item" style="top:780px"><span>Coconut Garlic Shrimp</span><span>$15.95</span></li>
    <li class="menu-item" style="top:818px"><span>Goat Cheese Stuffed Chicken</span><span>$14.95</span></li>
    <li class="menu-item" style="top:855px"><span>Chipotle Steak Wrap</span><span>$12.95</span></li>
    <li class="menu-item" style="top:892px"><span>Turkey Meatball Fettuccini</span><span>$13.45</span></li>
    <li class="menu-item" style="top:929px"><span>Chicken Alfredo</span><span>$13.45</span></li>
    <li class="menu-item" style="top:967px"><span>Chicken Parmesan</span><span>$13.95</span></li>
    <li class="menu-item" style="top:1004px"><span>Pesto Chicken Pasta</span><span>$13.45</span></li>
    <li class="menu-item" style="top:1041px"><span>Steak Bite and Green Stir Fry</span><span>$13.45</span></li>
    <li class="menu-item" style="top:1078px"><span>Asian Chicken Teriyaki</span><span>$13.45</span></li>
  </ul>
</main>
</body>
</html>
```